Pharmaceutical Manufacturing Services Advertisement

We need a new full page advertisement designed for publication in international magazines. We are a custom pharmaceutical manufacturing company and we help biotechnology companies scale up their drug development for clinical trials. The products we help manufacture are therapeutics for global healthcare problems.

Target Market(s)

Verott Bio is a privately owned contract development manufacturing organisation (CDMO) headquartered in Darra, QLD, Australia.

Our mission is to is to be a global leader in development and in the provision of contract manufacturing for active pharmaceutical ingredient processes.

Why we do what we Do:

To help advance Biotechnology Companies so that they can deliver innovative therapeutics
~ enabling patients to live longer, healthier and happier lives
~ which solves worldwide health problems

Verott Bio’s role is to develop, implement and scale up the production to deliver biologic medicines for patients in partnership with the biotechnology companies.

Industry/Entity Type

Biotechnology

Font styles to use
Sans Serif

Colors

Designer to choose colors to be used in the design.

Requirements
Must have
• Please see the script on the Word document. There are 4 optional Header Taglines. Additional ideas for multiple designs for the taglines welcomed.
• However preference is for either of the first two:
• 1. Building your vision for better healthcare
• 2. Bridging your vision for better healthcare
• File Specs:
• • All artwork should be submitted as high-resolution (300 min. dpi), press-ready PDF files
• • CMYK color only
• • Full page 8.25” x 10.812”; 209.55 x 274.62 mm
• • Live Area for all sizes: 0.25” (6.35 mm) inside the trim
• • Bleed Area for all sizes: Extends 0.125” (3.175 mm) from trim
Nice to have
• Modern Science look to inspire biotechnology companies to work with us.
• Search for images to use by keyword "recombinant dna"

```html
<!DOCTYPE html>
<html lang="en">
<head>
<meta charset="utf-8">
<title>Verott Bio – Building Your Vision for Better Healthcare</title>
<link rel="stylesheet" href="https://fonts.googleapis.com/css2?family=Oswald:wght@600;700&family=Archivo:wght@300;400;700&family=Roboto+Condensed:wght@400&display=swap">
<style>
  :root {
    --backdrop: #d4d4d6;
    --page: #ffffff;
    --lime: #c3d021;
    --lime-photo: rgba(190, 208, 30, 0.92);
    --navy: #005683;
    --ink: #1f1f1f;
    --muted: #5d6670;
  }
  * { margin: 0; padding: 0; box-sizing: border-box; }
  html, body {
    width: 1200px; height: 1200px; overflow: hidden;
    background: var(--backdrop);
  }
  .page {
    position: absolute; left: 169px; top: 35px;
    width: 862px; height: 1130px;
    background: var(--page);
    font-family: "Archivo", Arial, sans-serif;
    color: var(--ink);
  }
  .hero-photo {
    position: absolute; left: 0; top: 0; width: 862px; height: 551px;
    background:
      radial-gradient(ellipse at 35% 35%, #f1f1f5 0%, #dcdde4 35%, transparent 70%),
      linear-gradient(90deg, #b9bfc4 0%, #e3e5ea 30%, #eceef2 55%, #dfe3e6 100%);
  }
  .headline-panel {
    position: absolute; left: 422px; top: 0; width: 390px; height: 551px;
    background: linear-gradient(180deg, var(--lime-photo), rgba(178, 200, 40, 0.92));
    display: flex; flex-direction: column; align-items: center; justify-content: center;
    font-family: "Oswald", Impact, sans-serif; font-weight: 700; color: #fff;
    text-transform: uppercase; line-height: 1; padding-top: 12px;
  }
  .headline-panel .lead { font-size: 100px; letter-spacing: 1px; }
  .headline-panel .line { font-size: 74px; margin-top: 19px; letter-spacing: 0.5px; }
  .partner-band {
    position: absolute; left: 0; top: 551px; width: 862px; height: 47px;
    background: var(--lime);
    font-weight: 700; font-size: 29.5px; line-height: 47px;
    padding-left: 45px; color: #111;
  }
  .intro {
    position: absolute; left: 50px; top: 627px; width: 762px;
    font-weight: 300; font-size: 16.2px; line-height: 21px; text-align: justify;
  }
  .intro p + p { margin-top: 20px; }
  .offer-heading {
    position: absolute; height: 29px; width: 268px;
    color: #fff; font-weight: 700; font-size: 21px; line-height: 29px; padding-left: 47px;
  }
  .offer-heading svg { position: absolute; left: 0; top: 0; z-index: 0; }
  .offer-heading span { position: relative; z-index: 1; }
  .products-heading { left: 0; top: 813px; }
  .services-heading { left: 376px; top: 811px; }
  .offer-list {
    position: absolute; list-style: none;
    font-weight: 300; font-size: 16.5px; line-height: 20.3px;
  }
  .offer-list li { position: relative; padding-left: 47px; }
  .offer-list li::before {
    content: ""; position: absolute; left: 0; top: 8px;
    width: 6px; height: 6px; border-radius: 50%; background: #111;
  }
  .products-list { left: 49px; top: 856px; }
  .services-list { left: 425px; top: 855px; }
  .contact {
    position: absolute; left: 48px; top: 1003px;
    font-size: 22px; line-height: 27.5px; font-weight: 400;
  }
  .contact b { color: var(--navy); font-weight: 700; }
  .brand {
    position: absolute; left: 500px; top: 1024px;
  }
  .brand-name {
    font-family: "Archivo", Arial, sans-serif; font-weight: 700;
    font-size: 54px; line-height: 1; color: var(--navy); letter-spacing: 1px;
  }
  .brand-tagline {
    font-family: "Roboto Condensed", "Arial Narrow", sans-serif;
    font-size: 18.5px; color: var(--muted); margin-top: 10px; letter-spacing: 0.2px;
  }
  .footer-band {
    position: absolute; left: 0; bottom: 0; width: 862px; height: 23px;
    background: var(--lime);
  }
</style>
</head>
<body>
  <main class="page">
    <div class="hero-photo" role="img" aria-label="Soft-focus laboratory scene with a scientist in a white coat working at a bench with glassware"></div>
    <h1 class="headline-panel">
      <span class="lead">Building</span>
      <span class="line">Your Vision</span>
      <span class="line">For Better</span>
      <span class="line">Healthcare</span>
    </h1>
    <h2 class="partner-band">Your Partner in Early Phase Clinical Biomanufacturing</h2>

    <section class="intro">
      <p>We have been serving the pharmaceutical, biotechnology and veterinary industry for over 20 years so you can create innovative medicines for worldwide health problems.</p>
      <p>Get your therapeutics to the patient faster with cost-effective manufacturing for your GMP clinical trial material. We offer rapid technology transfer, scale-up development and manufacturing of microbial cell-derived proteins at up to 500L scale. We prepare your active pharmaceutical ingredient (API) products to a world class standard ready for clinical development.</p>
    </section>

    <h3 class="offer-heading products-heading">
      <svg width="268" height="29" viewBox="0 0 268 29"><polygon points="0,0 254,0 268,29 0,29" fill="#005683"/></svg>
      <span>Products:</span>
    </h3>
    <ul class="offer-list products-list">
      <li>Recombinant proteins</li>
      <li>Live Biotherapeutics</li>
      <li>Bacterial vaccines</li>
      <li>Plasmid DNA</li>
    </ul>

    <h3 class="offer-heading services-heading">
      <svg width="268" height="29" viewBox="0 0 268 29"><polygon points="0,0 254,0 268,29 0,29" fill="#005683"/></svg>
      <span>Services:</span>
    </h3>
    <ul class="offer-list services-list">
      <li>Bacterial / Yeast Fermentation</li>
      <li>Cell Banking</li>
      <li>Process Development/Scale-up</li>
      <li>cGMP Manufacture of biopharmaceutical APIs</li>
      <li>Stability Testing</li>
    </ul>

    <address class="contact" style="font-style:normal">
      <div><b>Visit</b> verottbio.com.au</div>
      <div><b>Australia</b> +61(7)35550148</div>
      <div><b>Email</b> enquiries@verottbio.com.au</div>
    </address>

    <div class="brand">
      <div class="brand-name">VEROTT BIO</div>
      <div class="brand-tagline">BIOPHARMACEUTICAL MANUFACTURING</div>
    </div>

    <div class="footer-band"></div>
  </main>
</body>
</html>
```